International Food Manufacturer in the need of a new business card and logo.

Our Company - Brightfield Provisions Ltd.

Our Industry - Food and Drink

We are a Wild Harvested Food Distributor / Manufacturer. We service the following food sectors: Supermarkets, Hotels, Restaurants, Cafes, Catering and all people looking to eat healthy food products.

Slogan - Wild harvested goodness for every table

Business card details -

48-52 Quarrow Lane
Ashby Meadow
London
NP7 3RD United Kingdom
Morven Tillick
+44 7700 900412 - UK
+971 50 5550137 - UAE
+38 067 555 0198 - Ukraine
morven@brightfieldprovisions.com
www.brightfieldprovisions.com

Goal - We are looking for a dynamic modern new look for our corporate image and a designer who can bring this new concept to our future food product designs. Please try to incorporate 3d hexagonal vector Imaging in your design concepts.

Target Market(s)

Industry/Entity Type

Food Service

Contact Information for Business Card

Brightfield Provisions Ltd.
48-52 Quarrow Lane
Ashby Meadow
London
NP7 3RD United Kingdom
Morven Tillick
+44 7700 900412 - UK
+971 50 5550137 - UAE

Font styles to use
Serif

Colors

Designer to choose colors to be used in the design.

Requirements
Must have
• Please read project description above.
Nice to have
Should not have

```html
<!DOCTYPE html>
<html lang="en">
<head>
<meta charset="utf-8">
<title>Brightfield Provisions Ltd. – Business Card</title>
<link rel="stylesheet" href="https://fonts.googleapis.com/css2?family=Libre+Bodoni:wght@400;700&family=Montserrat:wght@400;700&display=swap">
<style>
  :root {
    --card-navy: #134a74;
    --text-white: #ffffff;
    --hex-light: #5fc3ee;
    --hex-mid: #2a8fd0;
    --hex-deep: #1a6aa6;
  }
  html, body {
    margin: 0;
    padding: 0;
    overflow: hidden;
    background: var(--card-navy);
  }
  .card {
    position: relative;
    width: 1200px;
    height: 777px;
    background: var(--card-navy);
    color: var(--text-white);
    overflow: hidden;
  }
  .hex-decoration {
    position: absolute;
    left: 0;
    top: 0;
    width: 390px;
    height: 295px;
  }
  .brand {
    position: absolute;
    left: 496px;
    top: 67px;
    width: 600px;
    font-family: "Libre Bodoni", serif;
  }
  .brand-name {
    margin: 0;
    padding-left: 8px;
    font-size: 48px;
    font-weight: 400;
    line-height: 53px;
    white-space: nowrap;
  }
  .brand-slogan {
    margin: 13px 0 0;
    font-size: 30px;
    line-height: 37px;
    white-space: nowrap;
    padding-bottom: 10px;
    border-bottom: 4px solid var(--text-white);
  }
  .person-name {
    position: absolute;
    left: 466px;
    top: 232px;
    margin: 0;
    font-family: "Libre Bodoni", serif;
    font-size: 46px;
    font-weight: 400;
    white-space: nowrap;
  }
  .contact {
    position: absolute;
    left: 126px;
    width: 1000px;
    text-align: center;
    font-family: "Montserrat", sans-serif;
    white-space: nowrap;
  }
  .phones {
    top: 331px;
    margin: 0;
    padding: 0;
    list-style: none;
    font-size: 40px;
    font-weight: 700;
    line-height: 60px;
  }
  .web-details {
    top: 536px;
    margin: 0;
    font-size: 39px;
    font-weight: 400;
    line-height: 59px;
  }
  .address {
    top: 657px;
    margin: 0;
    font-style: normal;
    font-size: 38px;
    font-weight: 400;
    line-height: 48px;
  }
</style>
</head>
<body>
  <main class="card">
    <svg class="hex-decoration" role="img" aria-label="Faceted hexagonal decoration in shades of blue" viewBox="0 0 390 295" xmlns="http://www.w3.org/2000/svg">
      <defs>
        <radialGradient id="hexGlow" cx="0.35" cy="0.3" r="0.75">
          <stop offset="0" stop-color="#5fc3ee" stop-opacity="0.75"/>
          <stop offset="0.5" stop-color="#2a8fd0" stop-opacity="0.5"/>
          <stop offset="1" stop-color="#1a6aa6" stop-opacity="0"/>
        </radialGradient>
      </defs>
      <rect width="390" height="295" fill="url(#hexGlow)"/>
    </svg>

    <header class="brand">
      <h1 class="brand-name">Brightfield Provisions Ltd.</h1>
      <p class="brand-slogan">Wild harvested goodness for every table</p>
    </header>

    <h2 class="person-name">Morven Tillick</h2>

    <ul class="contact phones">
      <li>+44 7700 900412 - UK</li>
      <li>+971 50 5550137 - UAE</li>
      <li>+38 067 555 0198 - Ukraine</li>
    </ul>

    <p class="contact web-details">
      morven@brightfieldprovisions.com<br>
      www.brightfieldprovisions.com
    </p>

    <address class="contact address">
      48-52 Quarrow Lane Ashby Meadow London<br>
      NP7 3RD United Kingdom
    </address>
  </main>
</body>
</html>
```